Women's Health Company needs business card

We need a business card for a USA based women's health care company. We use digital technology to enhance therapy prescribed by clinicians for their patients

```html
<!DOCTYPE html>
<html lang="en">
<head>
<meta charset="utf-8">
<title>Velora Health – Business Card</title>
<link href="https://fonts.googleapis.com/css2?family=Montserrat:wght@400;500;700&display=swap" rel="stylesheet">
<style>
  :root {
    --bg: #2c2c2e;
    --purple: #5a2d86;
    --purple-soft: #6b3f96;
    --teal: #6fc1b9;
    --white: #ffffff;
  }
  * { margin: 0; padding: 0; box-sizing: border-box; }
  html, body {
    width: 1200px; height: 1186px; overflow: hidden;
    background: var(--bg);
    font-family: "Montserrat", sans-serif;
  }
  .card {
    position: absolute; left: 150px;
    width: 900px; height: 514px;
    border-radius: 34px; overflow: hidden;
  }
  .card--back { top: 64px; background: var(--purple); }
  .card--front { top: 608px; background: var(--white); }

  .back-wordmark {
    position: absolute; left: 0; right: 0; top: 200px;
    text-align: center;
    font-weight: 500; font-size: 92px; letter-spacing: 2px;
    color: var(--purple-soft);
  }

  .front-shape { position: absolute; inset: 0; }

  .front-logo {
    position: absolute; left: 70px; top: 178px;
    display: flex; align-items: center; gap: 14px;
    font-weight: 500; font-size: 50px; color: var(--teal);
  }
  .front-logo .dot {
    width: 16px; height: 16px; border-radius: 50%; background: var(--teal);
  }

  .details {
    position: absolute; right: 52px; top: 86px;
    text-align: right; color: var(--white);
  }
  .details .name { font-weight: 700; font-size: 30px; color: var(--teal); }
  .details .role { font-size: 18px; margin-top: 2px; }
  .details .address { font-size: 18px; line-height: 1.3; margin-top: 24px; }
  .contact { list-style: none; margin-top: 26px; font-size: 18px; line-height: 1.4; }
  .contact li { display: flex; justify-content: flex-end; align-items: center; gap: 14px; }
  .contact svg { width: 16px; height: 16px; }
</style>
</head>
<body>

<section class="card card--back" aria-label="Card back">
  <div class="back-wordmark">Velora Health</div>
</section>

<section class="card card--front" aria-label="Card front">
  <svg class="front-shape" viewBox="0 0 900 514" width="900" height="514" aria-hidden="true">
    <path d="M800 6 C560 14 520 220 440 330 C360 440 290 496 170 514" fill="none" stroke="var(--teal)" stroke-width="9"/>
    <path d="M900 0 L840 0 C590 14 548 224 466 336 C388 444 318 500 200 514 L900 514 Z" fill="var(--purple)"/>
  </svg>

  <div class="front-logo"><span class="dot"></span>Velora Health</div>

  <div class="details">
    <p class="name">Dana Whitfield</p>
    <p class="role">Managing Director</p>
    <p class="address">Birkenweg 214<br>20457 Hamburg</p>
    <ul class="contact">
      <li>+49 404 555 0123
        <svg viewBox="0 0 16 16"><path d="M3 1h3l1 4-2 1a9 9 0 0 0 5 5l1-2 4 1v3a2 2 0 0 1-2 2A13 13 0 0 1 1 3a2 2 0 0 1 2-2z" fill="var(--teal)"/></svg></li>
      <li>hello@velorahealth.com
        <svg viewBox="0 0 16 16"><rect x="1" y="3" width="14" height="10" rx="1" fill="var(--teal)"/><path d="M1 4l7 5 7-5" fill="none" stroke="var(--purple)" stroke-width="1.5"/></svg></li>
      <li>www.velorahealth.com
        <svg viewBox="0 0 16 16"><circle cx="8" cy="8" r="7" fill="var(--teal)"/><path d="M1 8h14M8 1c-3 4-3 10 0 14M8 1c3 4 3 10 0 14" fill="none" stroke="var(--purple)" stroke-width="1.2"/></svg></li>
    </ul>
  </div>
</section>

</body>
</html>
```